Welbourne Dental, P.C. New stationary and business card for modern Dental Office

We need a new stationary/envelope/business card design using our newly designed logo. We are looking for an upscale look. Our new logo is used on our signage, using black as the background and white for the lettering. We would like the stationary to have black, white, possible greys or silver. We are looking for a letterhead, envelope, and business card design for three different employees, as well as a 4th card, same design, but just general with no employee name.

Project Deadline Extended
Reason: We began this project in the middle of our move into our new office. Things got pretty hectic and we just didn't have the time to go through designs. We now settled in and finally eliminated the designs that didn't work for us. We would like to extend the project another 5 days, and then finalize our decision. Most of the submissions showed business cards alone, with no stationary designs. Our original request was for stationary and business cards. Please keep this in mind.

Target Market(s)

Dental patients expecting high quality, cosmetic dentistry

Industry/Entity Type

Business

Contact Information for Business Card

Will need a design using our logo. All cards will be the same, other than that one card will have Office Managers name, One for the Doctor, Hygienist,
1. Office Manager - Marisol Dubrovka
2. Hygienist - Kayleigh Morrow
3. Gordon T. Welbourne, D.D.S.
4. One general one with no staff names

Font styles to use
Other font styles liked:
• see upload

Colors
000000
1b1b1b
757575
c9c9c9
e8e8e8
ffffff

Requirements
Must have
• -Logo
• -Phone number (718)555-0193
• -Address: 4352 63rd Ave
• Lower Level
• Brooklyn, NY 11290

```html
<!DOCTYPE html>
<html lang="en">
<head>
<meta charset="utf-8">
<title>Welbourne Dental, P.C. — Stationery Set</title>
<link rel="stylesheet" href="https://fonts.googleapis.com/css2?family=Lato:wght@400;700&display=swap">
<style>
  :root {
    --backdrop: #cdcdcd;
    --slate: #5b5b5b;
    --slate-dark: #464646;
    --slate-line: #525252;
    --paper: #f0f0f0;
    --ink-soft: #757575;
    --ink-light: #a9a9a9;
    --ring: #9a9a9a;
    --ring-paper: #1b1b1b;
  }
  * { box-sizing: border-box; margin: 0; padding: 0; }
  html, body { width: 1200px; height: 1041px; overflow: hidden; }
  body {
    position: relative;
    background: var(--backdrop);
    font-family: "Lato", sans-serif;
  }
  .piece { position: absolute; overflow: hidden; }
  .slate { background: var(--slate); }

  /* brand mark: name + one plain circle beside it */
  .brand { position: absolute; display: flex; align-items: center; }
  .brand__name {
    font-family: "Lato", sans-serif;
    font-weight: 400;
    white-space: nowrap;
    color: var(--slate-dark);
  }
  .brand__ring { flex: none; border-radius: 50%; border: 2px solid var(--ring); }

  /* folder */
  .folder { left: 166px; top: 76px; width: 417px; height: 542px; border-radius: 3px; }
  .folder__spine { position: absolute; left: 20px; top: 0; bottom: 0; width: 7px; background: var(--slate-line); }
  .folder .brand { left: 150px; top: 112px; gap: 10px; }
  .folder .brand__name { font-size: 18px; }
  .folder .brand__ring { width: 40px; height: 40px; }

  /* letterhead */
  .letterhead { left: 615px; top: 94px; width: 403px; height: 524px; background: var(--paper); }
  .letterhead__edge { position: absolute; left: 0; right: 0; bottom: 0; height: 8px; background: var(--slate); }
  .letterhead .brand { left: 133px; top: 36px; gap: 6px; }
  .letterhead .brand__name { font-size: 10.5px; color: var(--ink-soft); }
  .letterhead .brand__ring { width: 22px; height: 22px; border-width: 1px; border-color: var(--ring-paper); }
  .letterhead__footer {
    position: absolute; left: 23px; right: 23px; bottom: 20px;
    display: flex; align-items: center; gap: 8px;
    font-size: 5.2px; color: var(--ink-soft); white-space: nowrap;
  }
  .letterhead__rule { flex: 1; height: 1px; background: var(--ink-light); }
  .letterhead__footer b { font-weight: 700; }

  /* envelopes */
  .envelope { top: 645px; width: 451px; height: 197px; }
  .envelope--front { left: 132px; }
  .envelope--front .brand { left: 23px; top: 38px; gap: 6px; }
  .envelope--front .brand__name { font-size: 11px; }
  .envelope--front .brand__ring { width: 24px; height: 24px; border-width: 1.5px; }
  .envelope__return {
    position: absolute; left: 23px; top: 165px;
    font-size: 5.2px; line-height: 7px; color: var(--ink-light); font-style: normal;
  }
  .envelope--back { left: 615px; }
  .envelope__flap { position: absolute; left: 18px; right: 18px; top: 65px; height: 1px; background: var(--slate-line); box-shadow: 0 1px 0 #666; }
  .envelope--back .brand { left: 166px; top: 24px; gap: 5px; }
  .envelope--back .brand__name { font-size: 8.5px; }
  .envelope--back .brand__ring { width: 18px; height: 18px; border-width: 1.5px; }

  /* business cards */
  .card { top: 870px; width: 167px; height: 96px; }
  .card--front { left: 416px; }
  .card--front .brand { left: 30px; top: 39px; gap: 5px; }
  .card--front .brand__name { font-size: 8.5px; }
  .card--front .brand__ring { width: 18px; height: 18px; border-width: 1.5px; }
  .card--back { left: 615px; }
  .card--back .brand { left: 14px; top: 20px; gap: 4px; }
  .card--back .brand__name { font-size: 7.5px; }
  .card--back .brand__ring { width: 15px; height: 15px; border-width: 1px; }
  .card__address {
    position: absolute; left: 14px; top: 70px;
    font-size: 4.2px; line-height: 5.4px; color: var(--ink-light); font-style: normal;
  }
  .card__address b { font-weight: 700; }
  .card__person { position: absolute; right: 14px; top: 72px; text-align: right; }
  .card__name { font-size: 5.2px; letter-spacing: 0.4px; color: #dcdcdc; text-transform: uppercase; }
  .card__role { font-size: 4.2px; color: var(--ink-light); margin-top: 1px; }
</style>
</head>
<body>

  <section class="piece folder slate" aria-label="Presentation folder">
    <div class="folder__spine"></div>
    <div class="brand">
      <span class="brand__name">Welbourne Dental, P.C.</span>
      <span class="brand__ring"></span>
    </div>
  </section>

  <section class="piece letterhead" aria-label="Letterhead">
    <div class="brand">
      <span class="brand__name">Welbourne Dental, P.C.</span>
      <span class="brand__ring"></span>
    </div>
    <footer class="letterhead__footer">
      <span class="letterhead__rule"></span>
      <span>4352 63rd Ave, Lower Level, Brooklyn, NY 11290 · <b>Phone:</b> (718)555-0193</span>
      <span class="letterhead__rule"></span>
    </footer>
    <div class="letterhead__edge"></div>
  </section>

  <section class="piece envelope envelope--front slate" aria-label="Envelope front">
    <div class="brand">
      <span class="brand__name">Welbourne Dental, P.C.</span>
      <span class="brand__ring"></span>
    </div>
    <address class="envelope__return">
      4352 63rd Ave, Lower Level<br>Brooklyn, NY 11290
    </address>
  </section>

  <section class="piece envelope envelope--back slate" aria-label="Envelope back">
    <div class="envelope__flap"></div>
    <div class="brand">
      <span class="brand__name">Welbourne Dental, P.C.</span>
      <span class="brand__ring"></span>
    </div>
  </section>

  <section class="piece card card--front slate" aria-label="Business card front">
    <div class="brand">
      <span class="brand__name">Welbourne Dental, P.C.</span>
      <span class="brand__ring"></span>
    </div>
  </section>

  <section class="piece card card--back slate" aria-label="Business card back">
    <div class="brand">
      <span class="brand__name">Welbourne Dental, P.C.</span>
      <span class="brand__ring"></span>
    </div>
    <address class="card__address">
      4352 63rd Ave, Lower Level<br>Brooklyn, NY 11290<br><b>Phone:</b> (718)555-0193
    </address>
    <div class="card__person">
      <div class="card__name">Jordan Pellworth</div>
      <div class="card__role">General Manager</div>
    </div>
  </section>

</body>
</html>
```